120ml Jar Label — Masculine Cosmetic Foot Balm for Cracked, Hardworking Heels

We need a print-ready wraparound label for a 120ml jar — a brown/amber glass jar with a black metal screw lid (file photo attached).

--DO NOT PUT A BARCODE ON THE LABEL PLEASE--
**PLEASE READ "PLAN HUDDLE PROJECT BRIEF FINAL.MD" IN ATTACHED FILES IF YOU ARE SUBMITTING A DESIGN.**

The label is 190mm wide × 40mm high.
We need files to be in an .ai format with a 2mm bleed at the end.
Social media handle: @bramblekeepnz (facebook, instagram and tiktok)

Bramble Keep is a New Zealand foot-care brand making practical, no-nonsense products for hardworking men whose jobs wreck their feet. Our flagship product, Ridge Mender Balm, helps fix thick, cracked, hardworking skin.

Brand color scheme and overview is all in the brief file. You may add some brand aligned colors outside of the specified hex codes as you see fit to make a great design. Feel free to remove the "Bramble Keep" text from the logo so Bramble Keep is not doubled up on the front of the label

The tone we want: direct, rugged, and credible — like a workwear brand, not a spa brand. Most cracked-heel products on the market lean soft and feminine; we want to stand apart by looking like a serious fix for a real problem, made in New Zealand.

Full legal requirements for New Zealand cosmetic labelling (ingredients, directions, net contents, origin, etc.) are listed in the attached brief document — these are non-negotiable and must stay legible.

Please see the label attached "Label spacing guide" for this project's rough spacing guide. This label is the same size and sits well on the jar. This label doesn't need to be spaced quite as much as the Verin Label

I want to run the design for a week - I feel 7 days is a good amount of time for designers to see the work, digest the brief and create something remarkable and memorable for Bramble Keep.

Target Market(s)

Working men in New Zealand whose jobs or lifestyle put heavy wear on their feet — tradies, farmers, hospital/shift workers, hunters, and outdoors people. Practical, value-driven buyers rather than luxury skincare shoppers.

Industry/Entity Type

Beauty / Health & Wellness / Cosmetics

Font styles to use
Sans Serif
Other font styles liked:
• Montserrat (bold, headings), Inter (regular, body)

Colors
00AB8E
00BBA5
67D7C9
C6EFE9
E9F9F6
FFC000
F8CF3A
FAE287
FDF2CF
FEFAEE

Requirements
Must have
• All NZ cosmetic labelling requirements from the attached brief (product name, tag line, net contents, ingredients, directions, storage, made in NZ) — legible and complete, not omitted for aesthetics Fits 190mm × 40mm wraparound format for a 120ml brown jar with black lid Uses our existing brand colors: Deep Olive #3C4A34, Bone White #F4EFE6, Terracotta Clay #C1683D, and Warm Grey #4A4540 (exact palette in attached brief) Uses Montserrat (headings) and Inter (body) or close equivalents Incorporates our existing shield-and-wing logo (attached) Brand name and product name clearly readable from a normal shelf/bathroom-cabinet distance
Nice to have
• A style that could extend into a hero/product photo later, similar to the NZ-hills-backdrop look on our website (screenshot attached) — not required for the label itself, just good to keep in mind Original icon work (e.g. a small soak/apply/sock icon set) if it fits the rugged brand feel A design that could work as a small back-label/wraparound split if the front can't fit everything at a readable size
Should not have
• No pastel colors, floral motifs, or delicate script fonts — this should never look like spa/luxury skincare. Don't introduce new brand colors outside the palette provided other than black.

```html
<!DOCTYPE html>
<html lang="en">
<head>
<meta charset="utf-8">
<title>Ridge Mender Balm – Jar Label</title>
<link href="https://fonts.googleapis.com/css2?family=Montserrat:wght@500;600;700;800&family=Inter:wght@400;500;600&display=swap" rel="stylesheet">
<style>
  :root {
    --canvas: #c2c2c2;
    --olive-top: #3d4a36;
    --olive-bottom: #1d261d;
    --bone: #f4efe6;
    --clay: #c1683d;
    --clay-band: #b8714b;
    --clay-soft: #d48a5e;
    --ink: #231f1c;
  }
  * { box-sizing: border-box; margin: 0; padding: 0; }
  html, body { width: 960px; height: 1200px; overflow: hidden; }
  body { background: var(--canvas); font-family: "Inter", sans-serif; color: var(--bone); }

  .label {
    position: absolute; left: 78px; top: 505px; width: 804px; height: 170px;
    box-shadow: 0 4px 10px rgba(0,0,0,.25);
  }
  .label__front {
    position: absolute; inset: 0 0 37px 0;
    background: linear-gradient(180deg, var(--olive-top) 0%, var(--olive-bottom) 100%);
  }
  .label__rule { position: absolute; left: 0; right: 0; bottom: 35px; height: 2px; background: var(--bone); }
  .label__band { position: absolute; left: 0; right: 0; bottom: 0; height: 35px; background: var(--clay-band); }

  /* claim + steps */
  .claim { position: absolute; left: 40px; top: 18px; width: 170px; text-align: center; }
  .claim__head { font-family: "Montserrat", sans-serif; font-weight: 800; font-size: 8.6px; line-height: 1.3; letter-spacing: .02em; }
  .claim__sub { font-size: 7.5px; margin-top: 1px; }
  .steps { position: absolute; left: 40px; top: 63px; width: 170px; display: flex; }
  .step { flex: 1; text-align: center; font-size: 6.2px; line-height: 1.3; }
  .step + .step { border-left: 1px solid rgba(244,239,230,.2); }
  .step svg { display: block; margin: 0 auto 2px; }
  .step__name { font-family: "Montserrat", sans-serif; font-weight: 700; color: var(--clay-soft); font-size: 6.4px; }

  /* product name */
  .title { position: absolute; left: 271px; top: 19px; font-family: "Montserrat", sans-serif; font-weight: 800; line-height: .92; }
  .title__line1 { font-size: 27px; color: var(--bone); }
  .title__line2 { font-size: 27px; color: var(--clay-soft); }
  .title__line3 { font-size: 15px; letter-spacing: .12em; color: var(--bone); margin-top: 2px; }
  .title__dash { width: 16px; height: 1.5px; background: var(--bone); margin: 5px 0 6px; }
  .tagline { font-family: "Montserrat", sans-serif; font-weight: 500; font-size: 12.5px; color: var(--bone); }

  /* brand mark stand-in */
  .brand { position: absolute; left: 450px; top: 54px; display: flex; align-items: center; gap: 6px; }
  .brand__dot { width: 14px; height: 14px; border-radius: 50%; background: var(--clay); }
  .brand__name { font-family: "Montserrat", sans-serif; font-weight: 800; font-size: 14px; color: var(--bone); }

  /* info */
  .info { position: absolute; left: 576px; top: 27px; width: 210px; font-size: 5.6px; line-height: 1.3; }
  .info__head { font-family: "Montserrat", sans-serif; font-weight: 700; color: var(--clay-soft); font-size: 6px; margin-bottom: 3px; }
  .info__block + .info__block { margin-top: 14px; }

  /* band content */
  .origin { position: absolute; left: 34px; top: 10px; display: flex; align-items: center; gap: 4px; font-size: 5.6px; line-height: 1.25; }
  .origin__map { width: 10px; height: 15px; background: var(--bone); border-radius: 3px 6px 2px 4px; opacity: .9; }
  .origin__lead { font-weight: 600; color: var(--ink); }
  .divider { position: absolute; left: 172px; top: 8px; width: 1px; height: 18px; background: var(--bone); }
  .social { position: absolute; left: 181px; top: 9px; font-size: 5.4px; line-height: 1.35; color: var(--ink); }
  .social__handle { font-weight: 600; color: var(--bone); font-size: 5.8px; }
  .net { position: absolute; left: 271px; top: 10px; font-family: "Montserrat", sans-serif; font-weight: 500; font-size: 10px; }
  .storage { position: absolute; left: 578px; top: 14px; font-size: 4.8px; color: var(--bone); }
  .storage b { font-family: "Montserrat", sans-serif; font-weight: 700; color: var(--ink); }
</style>
</head>
<body>
  <div class="label">
    <div class="label__front">
      <div class="claim">
        <p class="claim__head">CRACKED HEELS.<br>THICK SKIN. LONG DAYS.</p>
        <p class="claim__sub">Fix it. Protect it. Keep going.</p>
      </div>

      <div class="steps">
        <div class="step">
          <svg width="16" height="18" viewBox="0 0 16 18"><path d="M8 1 L15 3.5 V9 C15 13 11.5 15.5 8 17 C4.5 15.5 1 13 1 9 V3.5 Z" fill="none" stroke="#d48a5e" stroke-width="1.2"/><path d="M4.5 10 Q6 8.5 8 10 T11.5 10" fill="none" stroke="#f4efe6" stroke-width=".9"/><path d="M5 7 H11" stroke="#f4efe6" stroke-width=".9"/></svg>
          <p class="step__name">SOAK</p>
          <p>Warm soak<br>5-10 mins</p>
        </div>
        <div class="step">
          <svg width="16" height="18" viewBox="0 0 16 18"><path d="M8 1 L15 3.5 V9 C15 13 11.5 15.5 8 17 C4.5 15.5 1 13 1 9 V3.5 Z" fill="none" stroke="#d48a5e" stroke-width="1.2"/><circle cx="8" cy="9" r="2.6" fill="none" stroke="#f4efe6" stroke-width=".9"/><path d="M6 13 H10" stroke="#f4efe6" stroke-width=".9"/></svg>
          <p class="step__name">APPLY</p>
          <p>Massage balm<br>into heels</p>
        </div>
        <div class="step">
          <svg width="16" height="18" viewBox="0 0 16 18"><path d="M8 1 L15 3.5 V9 C15 13 11.5 15.5 8 17 C4.5 15.5 1 13 1 9 V3.5 Z" fill="none" stroke="#d48a5e" stroke-width="1.2"/><rect x="5" y="8" width="6" height="5" rx=".8" fill="none" stroke="#f4efe6" stroke-width=".9"/><path d="M6.3 8 V6.5 A1.7 1.7 0 0 1 9.7 6.5 V8" fill="none" stroke="#f4efe6" stroke-width=".9"/></svg>
          <p class="step__name">LOCK IT IN</p>
          <p>Wear socks<br>overnight</p>
        </div>
      </div>

      <div class="title">
        <p class="title__line1">RIDGE</p>
        <p class="title__line2">MENDER</p>
        <p class="title__line3">BALM</p>
        <div class="title__dash"></div>
        <p class="tagline">For Hardworking Soles</p>
      </div>

      <div class="brand">
        <span class="brand__dot"></span>
        <span class="brand__name">Bramble Keep</span>
      </div>

      <div class="info">
        <div class="info__block">
          <p class="info__head">INGREDIENTS</p>
          <p>Shea Butter, Beef Tallow, Beeswax, Grape Seed Oil, Vegetable Glycerin, Lanolin, Panthenol, Gluconolactone, Sodium Benzoate, Allantoin, Manuka Honey, Vitamin E, Tea Tree Essential Oil, Lemon Myrtle Essential Oil, Rosemary Oleoresin Extract</p>
        </div>
        <div class="info__block">
          <p class="info__head">DIRECTIONS</p>
          <p>Apply generously to clean, dry feet, focusing on heels and thick or cracked areas. For cracked heels, wear our moisture-locking socks overnight. Use daily.</p>
        </div>
      </div>
    </div>

    <div class="label__rule"></div>

    <div class="label__band">
      <div class="origin">
        <span class="origin__map" role="img" aria-label="Small outline map of New Zealand"></span>
        <p><span class="origin__lead">PROUDLY</span><br>NEW ZEALAND | MADE &amp; OWNED</p>
      </div>
      <div class="divider"></div>
      <p class="social">follow us on<br><span class="social__handle">@bramblekeepnz</span></p>
      <p class="net">120ml</p>
      <p class="storage"><b>STORAGE:</b>&nbsp; Keep out of direct sunlight. Best used within six months of opening.</p>
    </div>
  </div>
</body>
</html>
```